Zumbly - New Payment App for Student

Zum-bly - A Payment App for student to make payment, track own expenses and practice good dietary habits. The App theme is Fun and excitement.
Target User: Secondary Student aged 13-18
Look and Feel: Fun, excitement and simple.
Screen 1
Login to the app using thumbprints or password
Screen 2
Display the balance
Wallet balance >>> go to screen 3 to display transaction history
Gamification balance - points + badges >>> go to screen 3
Button to make payment
Screen 2-1
Allow them to do payment
Click “Pay”
Display QR code
scanning by merchant
Payment made
Notification received
The transaction history will be shown up
Screen 2-2
Allow them to top up (alternatively to parent Top-up using credit card)
Click “Top Up”
Display QR code
Pass the cash to merchant
scanning by merchant
Payment made
Notification received
The new balance will be shown up
Screen 3
Display more details on transaction history
Payment history + gamification history (gain/redeem points)
E.g. 14 Nov Canteen purchase $5.40
- Banana +30 points
- Milk +10 points
Screen 4 (play a game to earn point)
Introduce some trivial games (while waiting in line at cafeteria or school store) to gain some points
Crosswords
Puzzle
Screen 5 (Display achievements)
Leaderboard
Where the individual stands in the class
Where the class stands overall in school
Badges
Level
Achievements
For more, please go to our website http://www.zumbly-pay.example/
Target Market(s)
Secondary School Student aged 13-18
Industry/Entity Type
Education
Logo Text
zumbly
Look and feel

```html
<!DOCTYPE html>
<html lang="en">
<head>
<meta charset="utf-8">
<title>Zumbly – Sign in</title>
<link href="https://fonts.googleapis.com/css2?family=Lato:wght@400;700;900&display=swap" rel="stylesheet">
<style>
  :root {
    --bg: #ffffff;
    --ink: #111111;
    --title: #ff5a0a;
    --print-fill-top: #dcdcdc;
    --print-fill-bottom: #c6c6c6;
    --band-manual: #ff5200;
    --band-user: #e04800;
    --band-pass: #cf4200;
    --field-text: #ffe3d2;
    --cta-top: #ffd60a;
    --cta-bottom: #ffbf00;
    --cta-text: #4a2f00;
  }
  * { margin: 0; padding: 0; box-sizing: border-box; }
  html, body { width: 675px; height: 1200px; overflow: hidden; background: var(--bg); }
  body { font-family: "Lato", sans-serif; color: var(--ink); }

  .screen { position: relative; width: 675px; height: 1200px; overflow: hidden; }

  .status-bar {
    position: absolute; top: 0; left: 0; right: 0; height: 45px;
    display: flex; align-items: center; justify-content: space-between;
    padding: 0 14px; font-size: 22px; font-weight: 400;
  }
  .status-left, .status-right { display: flex; align-items: center; gap: 8px; width: 220px; }
  .status-right { justify-content: flex-end; }
  .status-time { font-weight: 700; }

  .title {
    position: absolute; top: 170px; left: 0; right: 0;
    text-align: center; font-size: 62px; font-weight: 900; color: var(--title);
    letter-spacing: 0.5px;
  }

  .touch-area {
    position: absolute; left: 237px; top: 461px; width: 200px; height: 276px;
    border-radius: 100px;
    background: linear-gradient(180deg, var(--print-fill-top), var(--print-fill-bottom));
  }

  .sign-in-panel { position: absolute; left: 0; right: 0; top: 875px; bottom: 0; }
  .band { display: flex; align-items: center; color: #fff; font-size: 25px; }
  .band-manual { height: 81px; background: var(--band-manual); justify-content: center; font-weight: 700; }
  .field { height: 80px; padding-left: 54px; color: var(--field-text); }
  .field-username { background: var(--band-user); }
  .field-password { background: var(--band-pass); }
  .cta {
    height: 84px; justify-content: center; font-weight: 700; color: var(--cta-text);
    background: linear-gradient(180deg, var(--cta-top), var(--cta-bottom));
  }
</style>
</head>
<body>
<main class="screen">
  <header class="status-bar">
    <div class="status-left">
      <svg width="58" height="12" viewBox="0 0 58 12" aria-hidden="true">
        <g fill="#111"><circle cx="6" cy="6" r="5"/><circle cx="17.5" cy="6" r="5"/><circle cx="29" cy="6" r="5"/><circle cx="40.5" cy="6" r="5"/><circle cx="52" cy="6" r="5"/></g>
      </svg>
      <span>Draftly</span>
      <svg width="24" height="18" viewBox="0 0 24 18" aria-hidden="true">
        <g fill="none" stroke="#111" stroke-width="2.6" stroke-linecap="round">
          <path d="M2 6.5 A14 14 0 0 1 22 6.5"/>
          <path d="M6 10.5 A8.5 8.5 0 0 1 18 10.5"/>
        </g>
        <circle cx="12" cy="15" r="2.4" fill="#111"/>
      </svg>
    </div>
    <div class="status-time">9:41 AM</div>
    <div class="status-right">
      <span>100%</span>
      <svg width="52" height="22" viewBox="0 0 52 22" aria-hidden="true">
        <rect x="1" y="1" width="45" height="20" rx="4" fill="none" stroke="#111" stroke-width="2"/>
        <rect x="4" y="4" width="39" height="14" rx="2" fill="#111"/>
        <rect x="47.5" y="7" width="3" height="8" rx="1.5" fill="#111"/>
      </svg>
    </div>
  </header>

  <h1 class="title">Sign in</h1>

  <div class="touch-area" role="img" aria-label="Fingerprint sign-in graphic"></div>

  <section class="sign-in-panel" aria-label="Manual sign in">
    <div class="band band-manual">Manual sign in</div>
    <div class="band field field-username">Username</div>
    <div class="band field field-password">Password</div>
    <div class="band cta">Sign in</div>
  </section>
</main>
</body>
</html>
```